Quarry IT Services Business Card

Quarry IT Services are a Perth based IT Services company. We would like to incorporate our company logo (attached) and stick with the blue that is in that design. I would like a clean look design that isn't too busy, yet creates a lasting image that is instantly recognisable in the recipients mind.

Target Market(s)

The target audience is small/medium business owners.

Industry/Entity Type

Business

Font styles to use
Serif
Sans Serif

Colors

Designer to choose colors to be used in the design.

Requirements
Must have
• The design should include:
Business name: Quarry IT Services
Directors Name: Darren Mowley
Phone Number: 0462 830 514
Email: support@quarryit.com.au
Website: www.quarryit.com.au

```html
<!DOCTYPE html>
<html lang="en">
<head>
<meta charset="utf-8">
<title>Quarry IT Services – Business Card Set</title>
<link rel="stylesheet" href="https://fonts.googleapis.com/css2?family=Arimo:wght@400;700&display=swap">
<style>
  :root {
    --brand-blue: #0a55a5;
    --paper: #ffffff;
    --backdrop: #e4e4e4;
    --ink-grey: #555555;
    --ink-dark: #333333;
  }
  * { box-sizing: border-box; margin: 0; padding: 0; }
  html, body {
    width: 1200px;
    height: 1051px;
    overflow: hidden;
    background: var(--backdrop);
    font-family: "Arimo", Arial, sans-serif;
  }
  .card-set {
    position: absolute;
    left: 45px;
    top: 245px;
    display: flex;
    gap: 60px;
  }
  .card {
    position: relative;
    width: 330px;
    height: 560px;
    background: var(--paper);
    box-shadow: 0 6px 18px rgba(0,0,0,0.18);
  }
  .card--blue { background: var(--brand-blue); }

  .card__web {
    position: absolute;
    top: 30px;
    right: 24px;
    font-size: 13px;
    color: var(--brand-blue);
  }
  .card--blue .card__web { color: var(--paper); }

  .wordmark {
    position: absolute;
    display: flex;
    align-items: center;
    gap: 10px;
    font-size: 24px;
    font-weight: 700;
    color: var(--brand-blue);
    white-space: nowrap;
  }
  .wordmark__square {
    width: 18px;
    height: 18px;
    background: var(--brand-blue);
  }
  .card--blue .wordmark { color: var(--paper); }
  .card--blue .wordmark__square { background: var(--paper); }

  .card--front .wordmark { left: 28px; bottom: 90px; }
  .card--back .wordmark { left: 28px; bottom: 90px; }
  .card--contact .wordmark { left: 28px; top: 270px; }

  .holder {
    position: absolute;
    top: 28px;
    right: 30px;
    text-align: right;
  }
  .holder__name {
    font-size: 17px;
    color: var(--ink-grey);
  }
  .holder__role {
    font-size: 12px;
    color: var(--brand-blue);
    margin-top: 3px;
  }
  .edge-tab {
    position: absolute;
    top: 26px;
    right: 0;
    width: 10px;
    height: 44px;
    background: var(--brand-blue);
  }

  .contact-list {
    position: absolute;
    left: 28px;
    bottom: 30px;
    list-style: none;
  }
  .contact-list li {
    display: flex;
    align-items: center;
    gap: 8px;
    font-size: 12px;
    color: var(--ink-dark);
    line-height: 18px;
  }
  .contact-list svg { width: 11px; height: 11px; flex: none; }
</style>
</head>
<body>
  <main class="card-set">
    <section class="card card--front" aria-label="Card front">
      <p class="card__web">www.quarryit.com.au</p>
      <div class="wordmark"><span class="wordmark__square"></span>Quarry IT Services</div>
    </section>

    <section class="card card--blue card--back" aria-label="Card back">
      <p class="card__web">www.quarryit.com.au</p>
      <div class="wordmark"><span class="wordmark__square"></span>Quarry IT Services</div>
    </section>

    <section class="card card--contact" aria-label="Contact card">
      <div class="holder">
        <p class="holder__name">Darren Mowley</p>
        <p class="holder__role">Director</p>
      </div>
      <span class="edge-tab"></span>
      <div class="wordmark"><span class="wordmark__square"></span>Quarry IT Services</div>
      <ul class="contact-list">
        <li>
          <svg viewBox="0 0 12 12" aria-hidden="true"><circle cx="6" cy="6" r="6" fill="var(--brand-blue)"/><path d="M4 3.2 L5 3 L5.6 4.6 L5 5.1 Q5.6 6.5 6.9 7 L7.4 6.4 L9 7 L8.8 8 Q6.5 8.6 4.7 6.6 Q3.4 5 4 3.2Z" fill="#fff"/></svg>
          0462 830 514
        </li>
        <li>
          <svg viewBox="0 0 12 12" aria-hidden="true"><circle cx="6" cy="6" r="6" fill="var(--brand-blue)"/><rect x="3" y="4" width="6" height="4.2" fill="#fff"/><path d="M3 4 L6 6.4 L9 4" stroke="var(--brand-blue)" stroke-width="0.7" fill="none"/></svg>
          support@quarryit.com.au
        </li>
        <li>
          <svg viewBox="0 0 12 12" aria-hidden="true"><circle cx="6" cy="6" r="6" fill="var(--brand-blue)"/><circle cx="6" cy="6" r="3.3" fill="none" stroke="#fff" stroke-width="0.8"/><path d="M2.7 6 H9.3 M6 2.7 V9.3" stroke="#fff" stroke-width="0.7"/></svg>
          www.quarryit.com.au
        </li>
      </ul>
    </section>
  </main>
</body>
</html>
```